Cryptocurrency Advisor Business Card

Velbridge Consulting Services is my company, which advises many projects in the ICO/Cryptocurrency industry. I'd like to get a sleek, preferably matte black or matte dark blue finish, business card with the company name (and simple logo w/ crypto feel) on one side and while the other side I'd like a small twitter and telegram logo together maybe separated by a / as it's the same, then an email and a phone logo so I can insert those specifics there (no address). Can have name then CEO section too. At the bottom of that section, find a place for more of a job description: ICO Advisor, World Champion Gamer, Esports Award Winner, Varlomark Expert. You can possibly design a simple logo or use something with a crypto twist or background, but nothing too complex. Rounded edges for printing not square.
Updates

Had personal issues taking a few days away from me being able to provide feedback and check designs, etc. Will be more active now finalizing design just needed few days from issue but all is sorted.

Target Market(s)

Cryptocurrency industry

Industry/Entity Type

Management Consulting

Contact Information for Business Card

Font styles to use
Sans Serif

Colors
5c5c5c
474747
757575
9d9d9d
aaaaaa
333333
0355a3

Requirements
Must have
• Refer to Details/Description
Nice to have
Should not have
• Address section

```html
<!DOCTYPE html>
<html lang="en">
<head>
<meta charset="utf-8">
<title>Velbridge Consulting – Business Card</title>
<link rel="stylesheet" href="https://fonts.googleapis.com/css2?family=Josefin+Sans:wght@300;400&family=Great+Vibes&display=swap">
<style>
  :root {
    --paper: #ffffff;
    --card: #0a0b0d;
    --accent: #0b4ce3;
    --ink-light: #ffffff;
    --ghost: #1a1c22;
    --shadow: rgba(0, 0, 0, 0.45);
  }
  html, body {
    margin: 0;
    padding: 0;
    width: 897px;
    height: 1200px;
    overflow: hidden;
    background: var(--paper);
  }
  .canvas {
    position: relative;
    width: 897px;
    height: 1200px;
  }
  .card {
    position: absolute;
    width: 749px;
    height: 429px;
    border-radius: 30px;
    background: var(--card);
    overflow: hidden;
    box-shadow: 0 22px 26px -8px var(--shadow), 0 4px 10px rgba(0,0,0,0.25);
  }
  .card--front { left: 57px; top: 47px; }
  .card--back  { left: 71px; top: 659px; }

  /* Front: company name */
  .brand-ring {
    position: absolute;
    left: 220px;
    top: 60px;
    width: 300px;
    height: 300px;
    border-radius: 50%;
    border: 14px solid var(--accent);
    box-sizing: border-box;
    opacity: 0.9;
  }
  .brand-name {
    position: absolute;
    margin: 0;
    font-family: "Josefin Sans", sans-serif;
    font-weight: 300;
    color: var(--accent);
    font-size: 44px;
    letter-spacing: 1px;
    line-height: 1;
  }
  .brand-name--first { left: 50px; top: 78px; }
  .brand-name--second { right: 50px; top: 330px; }

  /* Back: title block */
  .role {
    position: absolute;
    left: 49px;
    top: 48px;
    margin: 0;
    font-family: "Josefin Sans", sans-serif;
    font-weight: 400;
    font-size: 38px;
    color: var(--ink-light);
    letter-spacing: 1px;
    line-height: 1;
  }
  .job-line {
    position: absolute;
    left: 49px;
    top: 92px;
    margin: 0;
    font-family: "Great Vibes", cursive;
    font-size: 30px;
    color: var(--ink-light);
    line-height: 1;
  }
  .ghost-mark {
    position: absolute;
    left: 262px;
    top: 80px;
    width: 220px;
    height: 220px;
    border-radius: 50%;
    border: 10px solid var(--ghost);
    box-sizing: border-box;
  }

  /* Back: contacts */
  .contact-list {
    position: absolute;
    left: 49px;
    top: 216px;
    margin: 0;
    padding: 0;
    list-style: none;
  }
  .contact-item {
    display: flex;
    align-items: center;
    height: 24px;
    margin-bottom: 20px;
  }
  .contact-item:last-child { margin-bottom: 0; }
  .contact-icon {
    width: 24px;
    height: 24px;
    margin-right: 28px;
    flex: none;
  }
  .contact-text {
    font-family: "Josefin Sans", sans-serif;
    font-weight: 400;
    font-size: 20px;
    letter-spacing: 1.5px;
    color: var(--ink-light);
    line-height: 1;
    padding-top: 4px;
  }
  .contact-text--email { font-variant: small-caps; text-transform: lowercase; font-size: 22px; }

  .accent-band {
    position: absolute;
    left: 2px;
    right: 2px;
    top: 347px;
    height: 21px;
    background: var(--accent);
  }
</style>
</head>
<body>
<main class="canvas">

  <section class="card card--front" aria-label="Card front">
    <div class="brand-ring" aria-hidden="true"></div>
    <p class="brand-name brand-name--first">Velbridge</p>
    <p class="brand-name brand-name--second">Consulting</p>
  </section>

  <section class="card card--back" aria-label="Card back">
    <div class="ghost-mark" aria-hidden="true"></div>
    <h1 class="role">CEO</h1>
    <p class="job-line">World Champion Gamer</p>

    <ul class="contact-list">
      <li class="contact-item">
        <svg class="contact-icon" viewBox="0 0 24 24" aria-label="Phone">
          <circle cx="12" cy="12" r="11.5" fill="#ffffff"/>
          <circle cx="12" cy="12" r="9.5" fill="var(--accent)"/>
          <path d="M8.2 6.5l2 2.4-1.2 1.4c.8 1.7 2 2.9 3.7 3.7l1.4-1.2 2.4 2-1.2 1.8c-3.9-.4-7.1-3.6-7.5-7.5z" fill="#ffffff"/>
        </svg>
        <span class="contact-text">(xx) xxxx-xxxx</span>
      </li>
      <li class="contact-item">
        <svg class="contact-icon" viewBox="0 0 24 24" aria-label="Social account">
          <circle cx="12" cy="12" r="11.5" fill="#ffffff"/>
          <circle cx="12" cy="12" r="9.5" fill="var(--accent)"/>
        </svg>
        <span class="contact-text">(xx) xxxx-xxxx</span>
      </li>
      <li class="contact-item">
        <svg class="contact-icon" viewBox="0 0 24 24" aria-label="Messaging account">
          <circle cx="12" cy="12" r="11.5" fill="#ffffff"/>
          <circle cx="12" cy="12" r="9.5" fill="var(--accent)"/>
        </svg>
        <span class="contact-text contact-text--email">LORENIPSUM@IPSUMMAIL.COM</span>
      </li>
    </ul>

    <div class="accent-band" aria-hidden="true"></div>
  </section>

</main>
</body>
</html>
```